Business card design for Plumbing and Gas fitting company

We need a business card design for our plumbing and gas fitting company using the company logo and director details. Design should be modern and eye-catching however kept reasonably simple. This design should be targeted at commercial businesses/work so professionalism is key.

Target Market(s)

Commercial/business

Industry/Entity Type

Plumbing

Contact Information for Business Card

Warren Dohey
Director
027 581 9043
warren@vantorplumbingandgas.example
PO Box 7816
Palmerston North 4472

Font styles to use
Sans Serif

Requirements
Must have
• Logo
• Modern
• Kept simple
Nice to have
• Colour scheme based around logo

```html
<!DOCTYPE html>
<html lang="en">
<head>
<meta charset="utf-8">
<title>Vantor Plumbing &amp; Gas — Business Card</title>
<link rel="stylesheet" href="https://fonts.googleapis.com/css2?family=Open+Sans:wght@400;600;700&display=swap">
<style>
  :root {
    --backdrop: #e9e6e2;
    --card: #222222;
    --brand-blue: #1a7dc4;
    --brand-orange: #ef7d2a;
    --text-light: #c9c9c9;
    --icon-blue: #1a7dc4;
  }
  * { margin: 0; padding: 0; box-sizing: border-box; }
  html, body {
    width: 1200px;
    height: 1000px;
    overflow: hidden;
  }
  body {
    position: relative;
    background: var(--backdrop);
    font-family: "Open Sans", sans-serif;
  }
  .card {
    position: absolute;
    left: 267px;
    width: 665px;
    height: 395px;
    border-radius: 22px;
    background: var(--card);
    overflow: hidden;
  }
  .card--front { top: 75px; }
  .card--back { top: 535px; }

  .brand-name {
    display: flex;
    align-items: center;
    gap: 12px;
    color: var(--brand-blue);
    font-weight: 700;
    white-space: nowrap;
  }
  .brand-dot {
    flex: none;
    border-radius: 50%;
    background: var(--brand-orange);
  }
  .card--front .brand-name {
    position: absolute;
    left: 31px;
    top: 128px;
    font-size: 28px;
  }
  .card--front .brand-dot { width: 22px; height: 22px; }

  .contact {
    position: absolute;
    left: 32px;
    top: 220px;
    color: var(--text-light);
    font-size: 16px;
  }
  .contact__name {
    color: var(--brand-blue);
    font-weight: 700;
    font-size: 18px;
    letter-spacing: 0.3px;
    line-height: 24px;
  }
  .contact__role { line-height: 22px; margin-bottom: 16px; }
  .contact__line {
    display: flex;
    align-items: center;
    gap: 7px;
    line-height: 25px;
  }
  .contact__line svg { flex: none; }
  .contact__address { line-height: 25px; margin-top: 4px; }

  .accent-band {
    position: absolute;
    left: 0;
    bottom: 0;
    width: 100%;
    height: 12px;
  }

  .card--back .brand-name {
    position: absolute;
    left: 0;
    right: 0;
    top: 168px;
    justify-content: center;
    font-size: 42px;
    gap: 16px;
  }
  .card--back .brand-dot { width: 30px; height: 30px; }
</style>
</head>
<body>

  <section class="card card--front">
    <div class="brand-name">Vantor Plumbing &amp; Gas<span class="brand-dot"></span></div>

    <div class="contact">
      <p class="contact__name">WARREN DOHEY</p>
      <p class="contact__role">Managing Director</p>
      <p class="contact__line">
        <svg width="10" height="16" viewBox="0 0 10 16" aria-hidden="true">
          <rect x="1" y="1" width="8" height="14" rx="1.5" fill="none" stroke="var(--icon-blue)" stroke-width="1.5"/>
          <line x1="4" y1="12.5" x2="6" y2="12.5" stroke="var(--icon-blue)" stroke-width="1.2"/>
        </svg>
        027 581 9043
      </p>
      <p class="contact__line">
        <svg width="13" height="10" viewBox="0 0 13 10" aria-hidden="true">
          <rect x="0" y="0" width="13" height="10" rx="1" fill="var(--icon-blue)"/>
          <polyline points="0.5,0.8 6.5,5.5 12.5,0.8" fill="none" stroke="var(--card)" stroke-width="1.2"/>
        </svg>
        warren@vantorplumbingandgas.example
      </p>
      <p class="contact__address">PO Box 7816 Palmerston North 4472</p>
    </div>

    <svg class="accent-band" viewBox="0 0 665 12" preserveAspectRatio="none" aria-hidden="true">
      <polygon points="0,2 528,2 540,12 0,12" fill="var(--brand-blue)"/>
      <polygon points="535,2 665,2 665,12 547,12" fill="var(--brand-orange)"/>
    </svg>
  </section>

  <section class="card card--back">
    <div class="brand-name">Vantor Plumbing &amp; Gas<span class="brand-dot"></span></div>
  </section>

</body>
</html>
```